Billboard

I am a landscaping and irrigation company. I have purchased a billboard in a good part of town and I want a billboard that will stand out and show both colorful plantings/flowers and irrigation. My website is www.brimkettle.me

A phrase I have that of is showers and flowers, but I am not sure how to illustrate that since most stock pics are of just sprinkler heads and grass.

Target Market(s)

Target market is wealthy women

Industry/Entity Type

Landscaping

Requirements
Should not have
• Needs to look sharp and professional.

```html
<!DOCTYPE html>
<html lang="en">
<head>
<meta charset="utf-8">
<title>Brimkettle Billboard</title>
<link href="https://fonts.googleapis.com/css2?family=Cormorant+Garamond:wght@500;600;700&family=Great+Vibes&display=swap" rel="stylesheet">
<style>
  :root {
    --band: #000000;
    --ivory: #ffffff;
    --leaf-deep: #1f3312;
    --leaf-dark: #2f4a1c;
    --leaf: #4f7a2a;
    --leaf-bright: #6f9a38;
    --bloom: #d8604c;
    --bloom-red: #d42a2a;
    --spray: #eef2f4;
    --lawn: #8cb83e;
    --lavender: #7e68b0;
    --accent: #1f8a3a;
  }
  html, body {
    margin: 0;
    padding: 0;
    overflow: hidden;
    background: #ffffff;
  }
  .billboard {
    position: relative;
    width: 1200px;
    height: 600px;
    overflow: hidden;
    background: var(--band);
  }
  .photo-irrigation {
    position: absolute;
    left: 0; top: 0;
    width: 1200px; height: 204px;
    background:
      radial-gradient(ellipse 110px 80px at 190px 60px, rgba(238,242,244,.85), transparent 70%),
      radial-gradient(ellipse 120px 85px at 450px 55px, rgba(238,242,244,.85), transparent 70%),
      radial-gradient(ellipse 130px 90px at 705px 70px, rgba(238,242,244,.9), transparent 70%),
      radial-gradient(ellipse 120px 85px at 925px 75px, rgba(238,242,244,.85), transparent 70%),
      radial-gradient(ellipse 90px 70px at 1170px 20px, rgba(238,242,244,.8), transparent 70%),
      radial-gradient(ellipse 150px 80px at 60px 150px, var(--bloom), transparent 72%),
      radial-gradient(ellipse 110px 60px at 280px 175px, rgba(216,96,74,.85), transparent 72%),
      radial-gradient(ellipse 90px 50px at 400px 25px, rgba(216,96,74,.85), transparent 72%),
      radial-gradient(ellipse 80px 45px at 520px 30px, rgba(212,42,42,.75), transparent 72%),
      radial-gradient(ellipse 130px 70px at 870px 165px, rgba(216,96,74,.8), transparent 72%),
      radial-gradient(ellipse 160px 90px at 1110px 150px, var(--bloom), transparent 72%),
      radial-gradient(ellipse 90px 60px at 1060px 60px, rgba(216,96,74,.7), transparent 72%),
      linear-gradient(180deg, var(--leaf-bright) 0%, var(--leaf) 50%, var(--leaf-dark) 100%);
  }
  .tagline-band {
    position: absolute;
    left: 0; top: 204px;
    width: 1200px; height: 178px;
    background: var(--band);
  }
  .tagline {
    position: absolute;
    left: 0; right: 0; top: 268px;
    margin: 0;
    text-align: center;
    color: var(--ivory);
    font-family: "Cormorant Garamond", serif;
    font-weight: 500;
    font-size: 47px;
    line-height: 1;
    letter-spacing: 2.5px;
    text-transform: uppercase;
    white-space: nowrap;
  }
  .tagline .initial {
    font-family: "Great Vibes", cursive;
    font-size: 74px;
    text-transform: none;
    letter-spacing: 0;
    line-height: 0;
  }
  .photo-garden {
    position: absolute;
    left: 0; top: 382px;
    width: 1200px; height: 218px;
    background:
      linear-gradient(180deg, rgba(10,20,5,.75) 0%, rgba(10,20,5,0) 30%),
      radial-gradient(ellipse 120px 150px at 60px 170px, rgba(220,220,235,.55), transparent 72%),
      radial-gradient(ellipse 150px 80px at 260px 45px, var(--lavender), transparent 72%),
      radial-gradient(ellipse 140px 70px at 200px 180px, rgba(140,184,62,.8), transparent 72%),
      radial-gradient(ellipse 230px 150px at 790px 200px, var(--lawn), transparent 75%),
      radial-gradient(ellipse 170px 60px at 960px 55px, rgba(140,184,62,.85), transparent 72%),
      radial-gradient(ellipse 110px 90px at 1150px 120px, var(--bloom-red), transparent 72%),
      radial-gradient(ellipse 90px 60px at 1010px 170px, rgba(212,42,42,.8), transparent 72%),
      radial-gradient(ellipse 80px 50px at 1100px 40px, rgba(126,104,176,.7), transparent 72%),
      linear-gradient(180deg, var(--leaf-deep) 0%, var(--leaf-dark) 40%, var(--leaf) 100%);
  }
  .brand {
    position: absolute;
    left: 444px; top: 360px;
    width: 300px;
    text-align: center;
    color: var(--ivory);
    font-family: "Cormorant Garamond", serif;
    font-weight: 700;
  }
  .brand-name {
    display: inline-flex;
    align-items: center;
    gap: 10px;
    margin: 0;
    font-size: 44px;
    line-height: 1;
  }
  .brand-mark {
    width: 14px; height: 14px;
    background: var(--accent);
  }
  .brand-phone {
    display: block;
    margin-top: 8px;
    font-size: 26px;
    letter-spacing: 1px;
  }
</style>
</head>
<body>
  <main class="billboard">
    <div class="photo-irrigation" role="img" aria-label="Pop-up sprinkler heads spraying fans of water over red flowering shrubs"></div>
    <div class="tagline-band"></div>
    <h1 class="tagline"><span class="initial">S</span>imple showers. <span class="initial">F</span>abulous flowers.</h1>
    <div class="photo-garden" role="img" aria-label="Lush garden with lavender, colorful flower beds and a winding green lawn path"></div>
    <div class="brand">
      <p class="brand-name"><span class="brand-mark"></span>Brimkettle</p>
      <span class="brand-phone">(555) 014-2290</span>
    </div>
  </main>
</body>
</html>
```